We need a banner for this page on our website:
http://www.loganwhitfieldinsight.com/pathways-in-australian-erp/

Dimensions of the image should be approximately 1200 × 500

We are a research-based consultancy and this is a banner to subscribe to our paid content (about corporate technology systems).

Would like the final design to incorporate logo (attached files).
Updates

Banner must include the title "Pathways in Australian ERP"

thanks

Target Market(s)

Business professionals within medium to large Australian organisations and technology companies.

Requirements
Nice to have
• a call to action. something like "subscribe now" or similar. Happy to be directed based on designers customer experience perspective.

Could potentially include "Lifetime Membership"

If including a person consider a male and a female - not one or the other.

```html
<!DOCTYPE html>
<html lang="en">
<head>
<meta charset="utf-8">
<title>Pathways in Australian ERP – Logan Whitfield Insight</title>
<link rel="stylesheet" href="https://fonts.googleapis.com/css2?family=Open+Sans:wght@400;600;700&display=swap">
<style>
  :root {
    --band-blue: #00628f;
    --header-grey: #ececec;
    --footer-grey: #dcdcdc;
    --tab-grey: #d6d6d6;
    --panel-bg: #f5f5f5;
    --body-text: #454545;
    --nav-text: #3a5a78;
    --brand-blue: #2b4a8b;
    --accent-orange: #f39a1e;
    --cta-blue: #1ab4ec;
    --cta-text: #0b2a4a;
    --banner-deep: #06264f;
    --banner-mid: #0a5a9c;
    --banner-bright: #14b8ee;
    --white: #ffffff;
  }
  * { box-sizing: border-box; margin: 0; padding: 0; }
  html, body { width: 1200px; height: 800px; overflow: hidden; }
  body {
    position: relative;
    font-family: "Open Sans", Arial, sans-serif;
    background: var(--white);
    color: var(--body-text);
  }
  .top-band { position: absolute; left: 0; top: 0; width: 1200px; height: 93px; background: var(--band-blue); }
  .site-header {
    position: absolute; left: 0; top: 93px; width: 1200px; height: 94px;
    background: var(--header-grey); border-top: 1px solid #c9c9c9; border-bottom: 1px solid #d8d8d8;
  }
  .brand {
    position: absolute; left: 183px; top: 30px;
    display: flex; align-items: center; gap: 8px;
    font-size: 17px; font-weight: 600; color: var(--brand-blue); letter-spacing: .3px;
  }
  .brand-square { width: 22px; height: 22px; background: var(--brand-blue); }
  .top-nav {
    position: absolute; left: 789px; top: 7px; display: flex; gap: 17px;
    font-size: 10.5px; color: var(--nav-text); white-space: nowrap;
  }
  .search-box {
    position: absolute; left: 465px; top: 33px; width: 340px; height: 21px;
    background: var(--white); border: 1px solid #cfcfcf;
    font-size: 10px; color: #333; padding: 4px 3px;
  }
  .tabs { position: absolute; left: 472px; top: 69px; display: flex; gap: 4px; }
  .tab {
    height: 25px; padding: 0 17px; background: var(--tab-grey);
    font-size: 9.5px; font-weight: 700; color: #111; line-height: 25px;
  }
  .tab.is-active { background: var(--white); color: var(--accent-orange); font-weight: 600; width: 81px; text-align: center; padding: 0; }
  .content-panel {
    position: absolute; left: 337px; top: 207px; width: 596px; height: 510px;
    background: var(--panel-bg); border: 1px solid #e3e3e3; overflow: hidden;
  }
  .erp-banner {
    position: relative; margin: 1px; height: 248px; overflow: hidden;
    background: linear-gradient(180deg, var(--banner-deep) 0%, var(--banner-mid) 30%, var(--banner-bright) 48%, var(--banner-mid) 62%, var(--banner-deep) 100%);
  }
  .banner-brand {
    position: absolute; left: 25px; top: 24px; display: flex; align-items: center; gap: 6px;
    font-size: 14px; font-weight: 600; color: var(--white);
  }
  .banner-brand .brand-square { width: 17px; height: 17px; background: var(--white); }
  .banner-visual {
    position: absolute; left: 195px; top: 0; width: 400px; height: 248px;
    background: radial-gradient(circle at 72% 45%, rgba(150,220,250,.55) 0%, rgba(40,150,220,.35) 35%, rgba(10,60,120,0) 70%);
  }
  .banner-title {
    position: absolute; left: 37px; top: 160px;
    font-family: Arial, "Open Sans", sans-serif; font-size: 21px; color: var(--white);
  }
  .cta-subscribe {
    position: absolute; left: 37px; top: 221px; width: 274px; height: 32px;
    background: var(--cta-blue); border-radius: 16px 16px 0 0;
    font-family: Arial, "Open Sans", sans-serif; font-weight: 700; font-size: 13px;
    color: var(--cta-text); padding: 7px 0 0 13px;
  }
  .intro { padding: 17px 28px 0; text-align: center; font-size: 11.3px; line-height: 13.5px; }
  .intro p { margin-bottom: 14px; }
  .intro p.gap { margin-top: 20px; }
  .footer-strip { position: absolute; left: 0; top: 717px; width: 1200px; height: 28px; background: var(--footer-grey); }
  .bottom-band { position: absolute; left: 0; top: 745px; width: 1200px; height: 55px; background: var(--band-blue); }
</style>
</head>
<body>
  <div class="top-band"></div>

  <header class="site-header">
    <div class="brand"><span class="brand-square"></span>Logan Whitfield Insight</div>
    <nav class="top-nav">
      <span>Services</span>
      <span>Pathways in Australian ERP</span>
      <span>About LW</span>
      <span>Company Info</span>
      <span>How to Subscribe</span>
    </nav>
    <div class="search-box">Search...</div>
    <div class="tabs">
      <span class="tab is-active">Home Page</span>
      <span class="tab">Strategy</span>
      <span class="tab">Management</span>
      <span class="tab">Technology</span>
    </div>
  </header>

  <main class="content-panel">
    <section class="erp-banner">
      <div class="banner-visual" role="img" aria-label="Smiling businesswoman beside a glowing world map and data chart graphics"></div>
      <div class="banner-brand"><span class="brand-square"></span>Logan Whitfield Insight</div>
      <h1 class="banner-title">Pathways in Australian ERP</h1>
      <div class="cta-subscribe">Subscribe Now for Lifetime Membership</div>
    </section>

    <div class="intro">
      <p>LWI is an independent contracting and advisory company that specialises in providing strategic advice and operational support to organisations utilising, adopting or expanding use of enterprise solutions.</p>
      <p>We assist organisations to independently plan, guide and assure technology risk management approaches by working with your organisation in key governance, advisory, business analyst, or programme management positions.</p>
      <p class="gap">LWI is an independent contracting and advisory company that specialises in providing strategic advice and operational support to organisations utilising, adopting or expanding use of enterprise solutions.</p>
      <p>We assist organisations to independently plan, guide and assure technology risk management approaches by working with your organisation in key governance, advisory, business analyst, or programme management positions.</p>
      <p>With a long history in global business consulting through IT analyst firms including Northgate, Halverson Research, and Apex Group (Meridian), LWI has been involved first-hand in the opportunities, challenges and successes of significant corporate technology projects and investments.</p>
    </div>
  </main>

  <div class="footer-strip"></div>
  <div class="bottom-band"></div>
</body>
</html>
```